Social-Business Application (iOS)

App is very simillar to "Murmel" from AppHarbor

Please see the wireframes!

We need a design for application according to attached wireframes.
Social-Business application is a mobile app, that let's user to login, using ProNexa and browse through other users content (meme's). There are 2 home pages and 4 categories (displayed in wireframes). They are pretty simillar to each other. First one is called "Say Something" and the other one called "Ask Something". On "Say Something" page user is able to browse through meme's with pictures. There are several options to each meme, as well as reply to meme with your own meme.
"Ask Something" has only 2 differences.
1. There are always "?" in the end of each meme.
2. Only plain background with different colors are acceptable.
User is also able to create meme's to each home page and category.

There is no First or Last name display! Only following info should be displayed:
Location, Industry, Number of ProNexa contacts.

There is also a simple chat function, that provides the ability to chat with author of the meme. On the chat preview we will show the meme preview Instead of profile picture.

Please, ask your questions.
Updates

Please, send your examples.

Please check out "Murmel" application for better understanding of the functionality and overall idea

https://apps.harborstore-example.com/store/apps/details?id=qz.murmel

I will report to our admin, to change Designer Payment to Commited if we will have at least one screen example from you, guys.

Target Market(s)

regular users, business users.
Adult Audience, Professional Audience.

Industry/Entity Type

Business

Font styles to use
Other font styles liked:
• Helvetica Neue

Requirements
Must have
• Design must have all screens and elements that are displayed in attached photos (wireframes).
Flat style is required.
Following the iOS guidelines is required.
Nice to have
• Design example could show different ui colors for each of home pages ("Ask Something" and "Say Something") to easily indicate on what home page user is.
Should not have
• The design should not be overloaded and should not use serif fonts like Times New Roman.

```html
<!DOCTYPE html>
<html lang="en">
<head>
<meta charset="utf-8">
<title>iOS App Design — Social-Business App</title>
<link rel="stylesheet" href="https://fonts.googleapis.com/css2?family=Inter:wght@300;400;500;600&display=swap">
<style>
  :root{
    --stage:#141414;
    --purple:#9b10d6;
    --purple-deep:#7a0aa8;
    --ink-purple:#6e1a99;
    --feed-bg:#ebe9ef;
    --card:#ffffff;
    --ink:#222222;
    --muted:#777777;
    --badge:#e0262b;
    --dock:#161616;
    --white:#ffffff;
  }
  *{box-sizing:border-box;margin:0;padding:0}
  html,body{width:1200px;height:1000px;overflow:hidden;background:var(--stage)}
  body{position:relative;font-family:"Inter","Helvetica Neue",Arial,sans-serif;color:var(--white)}
  .board-title{position:absolute;top:58px;left:0;width:1200px;text-align:center;font-weight:300;font-size:58px;letter-spacing:-0.5px}
  .screen{position:absolute;top:216px;width:320px;height:568px;overflow:hidden;background:var(--feed-bg)}
  .screen--main{left:61px}
  .screen--detail{left:440px}
  .screen--comments{left:821px}
  .screen-label{position:absolute;top:826px;width:320px;text-align:center;font-size:27px;font-weight:300}
  .status-bar{position:absolute;top:0;left:0;width:320px;height:20px;background:var(--purple);font-size:11.5px;display:flex;align-items:center;padding:0 6px}
  .status-bar .carrier{display:flex;align-items:center;gap:4px}
  .status-bar .time{position:absolute;left:0;width:320px;text-align:center;font-weight:500}
  .status-bar .battery{margin-left:auto;display:flex;align-items:center;gap:4px}
  .nav-bar{position:absolute;top:20px;left:0;width:320px;height:44px;background:var(--purple);display:flex;align-items:center;justify-content:center}
  .nav-title{font-size:17px;font-weight:500}
  .nav-left{position:absolute;left:12px;top:11px}
  .nav-right{position:absolute;right:10px;top:11px}
  .badge{position:absolute;right:-4px;top:-8px;width:14px;height:14px;border-radius:50%;background:var(--badge);font-size:9px;text-align:center;line-height:14px}
  .segments{position:absolute;top:64px;left:0;width:320px;height:44px;background:var(--purple-deep);display:flex}
  .segment{flex:1;display:flex;align-items:center;justify-content:center;font-size:13.5px;font-weight:300}
  .segment + .segment{border-left:1px solid rgba(255,255,255,.25)}
  .card{position:absolute;width:146px;background:var(--card)}
  .card-meta{height:20px;font-size:8.5px;color:var(--ink-purple);padding:5px 6px 0}
  .card-photo{height:144px}
  .card-stats{height:21px;display:flex;align-items:center;font-size:8.5px;color:var(--muted);padding:0 6px;gap:3px}
  .card-stats svg{fill:var(--ink)}
  .card-stats .age{margin-left:auto;display:flex;align-items:center;gap:3px}
  .card-stats .gap{width:10px}
  .author-box{position:absolute;top:76px;left:10px;width:300px;height:42px;background:var(--card);color:var(--ink-purple);font-size:14px;display:flex;align-items:center;justify-content:center}
  .meme-photo{position:absolute;top:131px;left:10px;width:300px;height:373px}
  .action-bar{position:absolute;top:514px;left:10px;width:300px;height:43px;background:var(--card);display:flex}
  .action{flex:1;display:flex;align-items:center;justify-content:center;gap:5px;font-size:11px;color:var(--muted)}
  .action + .action{border-left:1px solid #e3e3e3}
  .action svg{fill:var(--ink)}
  .carousel-shade{position:absolute;top:332px;left:0;width:320px;height:172px;background:rgba(0,0,0,.82)}
  .carousel .card{top:364px;width:106px}
  .carousel .card-meta{height:16px;font-size:6px;padding:4px 4px 0;white-space:nowrap;overflow:hidden}
  .carousel .card-photo{height:108px}
  .carousel .card-stats{height:16px;font-size:6px;padding:0 4px}
  .dock{position:absolute;top:504px;left:0;width:320px;height:64px;background:var(--dock);display:flex}
  .dock-item{flex:1;display:flex;align-items:center;justify-content:center}
  .dock-item svg{fill:var(--white)}
</style>
</head>
<body>
<svg width="0" height="0" style="position:absolute" aria-hidden="true">
  <symbol id="i-heart" viewBox="0 0 24 22"><path d="M12 21.5 10.3 20C4.2 14.4 0 10.7 0 6.3 0 2.7 2.8 0 6.3 0c2 0 4 .9 5.7 2.4C13.7.9 15.7 0 17.7 0 21.2 0 24 2.7 24 6.3c0 4.4-4.2 8.1-10.3 13.7z"/></symbol>
  <symbol id="i-comment" viewBox="0 0 24 22"><path d="M1 1h22v15H11l-5 5v-5H1z"/><circle cx="7" cy="8.5" r="1.5" fill="#fff"/><circle cx="12" cy="8.5" r="1.5" fill="#fff"/><circle cx="17" cy="8.5" r="1.5" fill="#fff"/></symbol>
  <symbol id="i-clock" viewBox="0 0 20 20"><circle cx="10" cy="10" r="10"/><path d="M10 4v6l4 3" stroke="#fff" stroke-width="2" fill="none"/></symbol>
  <symbol id="i-mail" viewBox="0 0 26 18"><rect x="1" y="1" width="24" height="16" fill="none" stroke="currentColor" stroke-width="2"/><path d="M1 1l12 9 12-9M1 17l9-7M25 17l-9-7" fill="none" stroke="currentColor" stroke-width="2"/></symbol>
  <symbol id="i-share" viewBox="0 0 24 24"><circle cx="19" cy="4" r="3.5"/><circle cx="5" cy="12" r="3.5"/><circle cx="19" cy="20" r="3.5"/><path d="M19 4 5 12l14 8" stroke="currentColor" stroke-width="2" fill="none"/></symbol>
  <symbol id="i-back" viewBox="0 0 12 20"><path d="M10 2 2 10l8 8" stroke="#fff" stroke-width="2.5" fill="none"/></symbol>
  <symbol id="i-grid" viewBox="0 0 22 22"><g fill="#fff"><circle cx="3" cy="3" r="2.5"/><circle cx="11" cy="3" r="2.5"/><circle cx="19" cy="3" r="2.5"/><circle cx="3" cy="11" r="2.5"/><circle cx="11" cy="11" r="2.5"/><circle cx="19" cy="11" r="2.5"/><circle cx="3" cy="19" r="2.5"/><circle cx="11" cy="19" r="2.5"/><circle cx="19" cy="19" r="2.5"/></g></symbol>
  <symbol id="i-wifi" viewBox="0 0 14 10"><path d="M1 4a9 9 0 0 1 12 0M3.5 6.5a5 5 0 0 1 7 0" stroke="#fff" stroke-width="1.5" fill="none"/><circle cx="7" cy="8.7" r="1.3" fill="#fff"/></symbol>
  <symbol id="i-battery" viewBox="0 0 26 11"><rect x=".5" y=".5" width="22" height="10" rx="2" fill="none" stroke="#fff"/><rect x="2" y="2" width="19" height="7" fill="#fff"/><rect x="23.5" y="3.5" width="2" height="4" fill="#fff"/></symbol>
</svg>

<h1 class="board-title">iOS App Design</h1>

<!-- Main screen -->
<section class="screen screen--main">
  <div class="status-bar">
    <span class="carrier">●●●○○ LUMA <svg width="13" height="10"><use href="#i-wifi"/></svg></span>
    <span class="time">4:21 PM</span>
    <span class="battery">100% <svg width="26" height="11"><use href="#i-battery"/></svg></span>
  </div>
  <header class="nav-bar">
    <svg class="nav-left" width="22" height="22"><use href="#i-grid"/></svg>
    <span class="nav-title">Latest</span>
    <span class="nav-right" style="color:#fff"><svg width="26" height="18"><use href="#i-mail"/></svg><span class="badge">1</span></span>
  </header>
  <nav class="segments"><span class="segment">Say Something</span><span class="segment">Ask Something</span></nav>

  <article class="card" style="left:10px;top:117px">
    <div class="card-meta">Phil, Tourism, 555-010-4321</div>
    <div class="card-photo" role="img" aria-label="Meme photo: beach handstand with legs above water" style="background:linear-gradient(#bcd3e6,#8aaec6 55%,#c9b79a)"></div>
    <div class="card-stats"><svg width="10" height="9"><use href="#i-heart"/></svg>4<span class="gap"></span><svg width="10" height="9"><use href="#i-comment"/></svg>7<span class="age"><svg width="9" height="9"><use href="#i-clock"/></svg>58s ago</span></div>
  </article>
  <article class="card" style="left:165px;top:117px">
    <div class="card-meta">USA, Music, 555-014-0000</div>
    <div class="card-photo" role="img" aria-label="Meme photo: stage performance scene with caption" style="background:linear-gradient(#1c1c1c,#3a3234 60%,#6b5a55)"></div>
    <div class="card-stats"><svg width="10" height="9"><use href="#i-heart"/></svg>78<span class="gap"></span><svg width="10" height="9"><use href="#i-comment"/></svg>54<span class="age"><svg width="9" height="9"><use href="#i-clock"/></svg>2m ago</span></div>
  </article>
  <article class="card" style="left:10px;top:312px">
    <div class="card-meta">Phil, Sports, 555-019-4567</div>
    <div class="card-photo" role="img" aria-label="Meme photo: portrait on blue background with caption" style="background:linear-gradient(#3c55a8,#2d4391)"></div>
    <div class="card-stats"><svg width="10" height="9"><use href="#i-heart"/></svg>7<span class="gap"></span><svg width="10" height="9"><use href="#i-comment"/></svg>12<span class="age"><svg width="9" height="9"><use href="#i-clock"/></svg>7m ago</span></div>
  </article>
  <article class="card" style="left:165px;top:312px">
    <div class="card-meta">China, Industry, 555-012-2233</div>
    <div class="card-photo" role="img" aria-label="Meme photo: two officials talking with caption" style="background:linear-gradient(#7d8a78,#5b6a52 60%,#37404a)"></div>
    <div class="card-stats"><svg width="10" height="9"><use href="#i-heart"/></svg>10<span class="gap"></span><svg width="10" height="9"><use href="#i-comment"/></svg>4<span class="age"><svg width="9" height="9"><use href="#i-clock"/></svg>12m ago</span></div>
  </article>
  <article class="card" style="left:10px;top:507px">
    <div class="card-meta">Phil, Automotive, 555-77-0000</div>
    <div class="card-photo" role="img" aria-label="Meme photo: street with a colourful bus" style="background:linear-gradient(#c7d6c0,#7aa0b0)"></div>
  </article>
  <article class="card" style="left:165px;top:507px">
    <div class="card-meta">Phil, Food, 555-022-7878</div>
    <div class="card-photo" role="img" aria-label="Meme photo: snack close-up with caption" style="background:linear-gradient(#c9b98c,#a8905a)"></div>
  </article>
</section>
<p class="screen-label" style="left:56px">Main Screen</p>

<!-- Meme details -->
<section class="screen screen--detail">
  <div class="status-bar">
    <span class="carrier">●●●○○ LUMA <svg width="13" height="10"><use href="#i-wifi"/></svg></span>
    <span class="time">4:21 PM</span>
    <span class="battery">100% <svg width="26" height="11"><use href="#i-battery"/></svg></span>
  </div>
  <header class="nav-bar">
    <svg class="nav-left" width="12" height="20" style="top:12px"><use href="#i-back"/></svg>
    <span class="nav-title">Meme #0728</span>
    <span class="nav-right" style="color:#fff"><svg width="26" height="18"><use href="#i-mail"/></svg><span class="badge">1</span></span>
  </header>
  <div class="author-box">Phil, Tourism, 555-010-4321</div>
  <div class="meme-photo" role="img" aria-label="Meme collage: large bat in forest trees above, campfire cooking scene below, with captions" style="background:linear-gradient(#55603f,#6e6250 30%,#8f8f8a 50%,#2a2a22 55%,#3b3020 75%,#c66a1e 90%,#5a4a3a)"></div>
  <div class="action-bar">
    <span class="action"><svg width="26" height="23"><use href="#i-heart"/></svg>700 Likes</span>
    <span class="action"><svg width="26" height="24"><use href="#i-comment"/></svg>9 Comments</span>
    <span class="action" style="color:#222"><svg width="26" height="26"><use href="#i-share"/></svg><span style="color:var(--muted)">Share</span></span>
  </div>
</section>
<p class="screen-label" style="left:436px">Meme Details</p>

<!-- Display comments -->
<section class="screen screen--comments">
  <div class="status-bar">
    <span class="carrier">●●●○○ LUMA <svg width="13" height="10"><use href="#i-wifi"/></svg></span>
    <span class="time">4:21 PM</span>
    <span class="battery">100% <svg width="26" height="11"><use href="#i-battery"/></svg></span>
  </div>
  <header class="nav-bar">
    <svg class="nav-left" width="12" height="20" style="top:12px"><use href="#i-back"/></svg>
    <span class="nav-title">Meme #0728</span>
    <span class="nav-right" style="color:#fff"><svg width="26" height="18"><use href="#i-mail"/></svg><span class="badge">1</span></span>
  </header>
  <div class="author-box">Phil, Tourism, 555-010-4321</div>
  <div class="meme-photo" role="img" aria-label="Meme collage: large bat in forest trees above, campfire cooking scene below, with captions" style="background:linear-gradient(#55603f,#6e6250 30%,#8f8f8a 50%,#2a2a22 55%,#3b3020 75%,#c66a1e 90%,#5a4a3a)"></div>
  <div class="carousel-shade"></div>
  <div class="carousel">
    <article class="card" style="left:-26px">
      <div class="card-meta">Phil, Food, 555-022-7878</div>
      <div class="card-photo" role="img" aria-label="Reply meme: snack close-up" style="background:linear-gradient(#c9b98c,#a8905a)"></div>
      <div class="card-stats"><svg width="7" height="6"><use href="#i-heart"/></svg>4<span class="age"><svg width="6" height="6"><use href="#i-clock"/></svg>12m ago</span></div>
    </article>
    <article class="card" style="left:106px">
      <div class="card-meta">Phil, Tourism, 555-010-4321</div>
      <div class="card-photo" role="img" aria-label="Reply meme: beach handstand" style="background:linear-gradient(#bcd3e6,#8aaec6 55%,#c9b79a)"></div>
      <div class="card-stats"><svg width="7" height="6"><use href="#i-heart"/></svg>4<span class="gap"></span><svg width="7" height="6"><use href="#i-comment"/></svg>7<span class="age"><svg width="6" height="6"><use href="#i-clock"/></svg>58s ago</span></div>
    </article>
    <article class="card" style="left:239px">
      <div class="card-meta">Phil, Automotive, 555-77-0000</div>
      <div class="card-photo" role="img" aria-label="Reply meme: colourful bus on a street" style="background:linear-gradient(#cfd8c8,#5aa0b8 60%,#8a7a5a)"></div>
      <div class="card-stats"><svg width="7" height="6" style="fill:var(--purple)"><use href="#i-heart"/></svg>7<span class="gap"></span><svg width="7" height="6"><use href="#i-comment"/></svg>12</div>
    </article>
  </div>
  <nav class="dock">
    <span class="dock-item"><svg width="26" height="23"><use href="#i-heart"/></svg></span>
    <span class="dock-item"><svg width="26" height="24"><use href="#i-comment"/></svg></span>
    <span class="dock-item" style="color:#fff"><svg width="26" height="18"><use href="#i-mail"/></svg></span>
  </nav>
</section>
<p class="screen-label" style="left:824px">Display Comments</p>
</body>
</html>
```